Construction Company Facebook Banner

We are a small residential building company, building mostly new homes, renovations, extensions. our social media needs an uplift to look more professional.
I have no photos I wish to use in the banner as of yet however I have included the company logo, and the business card design which has some details.
I would like something simple but professional.
The banner does not need to have email, phone number, services provided etc. all of this is available on the facebook page itself. Something simple and clean please.
Industry/Entity Type
Construction
Requirements
Should not have
- Images of people, QR Code

```html
<!DOCTYPE html>
<html lang="en">
<head>
<meta charset="utf-8">
<title>Kestrel Homes – Facebook Cover</title>
<link href="https://fonts.googleapis.com/css2?family=Roboto:wght@400;500;700&display=swap" rel="stylesheet">
<style>
  :root {
    --page-bg: #eeeff1;
    --brand-green: #2eb24b;
    --ink: #262626;
    --muted: #6b6b6b;
    --white: #ffffff;
    --roof: #b8aea2;
    --sky: #5c93d6;
    --wall: #9a9ea3;
  }
  * { margin: 0; padding: 0; box-sizing: border-box; }
  html, body {
    width: 1200px;
    height: 1200px;
    overflow: hidden;
    background: var(--page-bg);
    font-family: "Roboto", Arial, sans-serif;
  }
  .cover {
    position: absolute;
    left: 30px;
    top: 378px;
    width: 1140px;
    height: 444px;
    overflow: hidden;
    box-shadow: 0 18px 40px rgba(0,0,0,0.18);
  }
  .cover-photo {
    position: absolute;
    inset: 0;
    background:
      linear-gradient(180deg, rgba(255,255,255,0) 0%, rgba(230,220,205,0.35) 100%),
      linear-gradient(90deg, var(--roof) 0%, #d9d3cb 22%, #f4f4f2 42%, #f7f8fa 60%, #c9d7ea 78%, var(--sky) 100%);
  }
  .cover-photo::after {
    content: "";
    position: absolute;
    right: 0;
    top: 40%;
    width: 24%;
    height: 60%;
    background: linear-gradient(90deg, rgba(154,158,163,0) 0%, var(--wall) 60%);
    opacity: 0.8;
  }
  .cover-glow {
    position: absolute;
    inset: 0;
    background: radial-gradient(ellipse 42% 70% at 50% 50%, rgba(255,255,255,0.95) 0%, rgba(255,255,255,0.7) 55%, rgba(255,255,255,0) 100%);
  }
  .brand {
    position: absolute;
    left: 0;
    right: 0;
    top: 84px;
    display: flex;
    flex-direction: column;
    align-items: center;
  }
  .brand-square {
    width: 40px;
    height: 40px;
    background: var(--brand-green);
    margin-bottom: 18px;
  }
  .brand-name {
    color: var(--ink);
    font-weight: 500;
    text-transform: uppercase;
    text-align: center;
    line-height: 1;
  }
  .brand-name .line-main { display: block; font-size: 50px; letter-spacing: 1px; }
  .brand-name .line-sub { display: block; font-size: 25px; letter-spacing: 1px; margin-top: 4px; }
  .services {
    position: absolute;
    left: 50%;
    top: 280px;
    transform: translateX(-50%);
    height: 51px;
    padding: 0 20px;
    background: var(--brand-green);
    border-radius: 26px;
    display: flex;
    align-items: center;
    gap: 20px;
    white-space: nowrap;
  }
  .service {
    color: var(--white);
    font-weight: 700;
    font-size: 24px;
  }
  .service-dot {
    width: 15px;
    height: 15px;
    border-radius: 50%;
    background: var(--white);
  }
  .tagline {
    position: absolute;
    left: 0;
    right: 0;
    top: 343px;
    text-align: center;
    font-size: 23px;
    font-weight: 400;
    color: var(--muted);
  }
</style>
</head>
<body>
  <section class="cover">
    <div class="cover-photo" role="img" aria-label="Photo of a new home with a gabled carport roof on the left and a grey garage door and driveway on the right under a blue sky"></div>
    <div class="cover-glow"></div>

    <div class="brand">
      <div class="brand-square"></div>
      <p class="brand-name">
        <span class="line-main">Kestrel Homes</span>
        <span class="line-sub">and Developments Pty Ltd</span>
      </p>
    </div>

    <div class="services">
      <span class="service">Your service 01</span>
      <span class="service-dot"></span>
      <span class="service">Your service 02</span>
      <span class="service-dot"></span>
      <span class="service">Your service 03</span>
    </div>

    <p class="tagline">Lorem ipsum, no eos, vim an unum aliquam perfecto.</p>
  </section>
</body>
</html>
```